Plastic Surgeon Stationery Design for a female surgeon

I would like a modern-classic stationery design ... I'm a 46 y.o plastic surgeon from Brasil and recently changed my life ( I was a navy surgeon for 18 years) . Now I'm on my office in Rio de Janeiro and I would like a classy design .
I have a fanpage with 76.000 followers on facebook and 12000 on instagram, and I love social media.
I like the colours like brown, beige ( something that I can use with the picture I'm attaching).

Target Market(s)

people who loves beauty, life

Industry/Entity Type

Plastic

Contact Information for Business Card

Dra Luciana Prado de Macedo e Costa
Cirurgiã Plástica - Estética e Reconstrutiva
CRM 47.38195- 2 RQE 5716

Av. dos Coqueirais 3482 bl 03 cob 01
Jardim Solaris - RJ - CEP 22874-000

Cons : (21) 2738-5164 Celular: (21) 97352-4618
lucianaprado@correionuvem.com

Logo Text

Luciana de Macedo - Cirurgiã Plástica

Font styles to use
Other font styles liked:
• I like the Scrip fonts but I'm open to sugestions

Colors
fbe7d2
ffffff
f8ba93
fee3d4
f9ba93
919191
757575
5c5c5c
9d9d9d

Requirements
Must have
• I would like my logo with something related to my initials and easy to use on merchandising stuff like pens, bags ...
Nice to have
• things related to happiness , graffic contents ( I love forms)
Should not have
• the plastic surgery cliches like female bodies , breasts , human parts ...

```html
<!DOCTYPE html>
<html lang="pt-BR">
<head>
<meta charset="utf-8">
<title>Luciana de Macedo – Cartão de Visita</title>
<link rel="stylesheet" href="https://fonts.googleapis.com/css2?family=Source+Sans+3:wght@400&display=swap">
<style>
  :root {
    --backdrop: #2e1d14;
    --card-white: #ffffff;
    --peach: #f8ba93;
    --peach-soft: #fbe7d2;
    --blush: #fee3d4;
    --sunset-rose: #e9a596;
    --sunset-gold: #fcd9a8;
    --text-grey: #5c5c5c;
  }
  * { box-sizing: border-box; margin: 0; padding: 0; }
  html, body {
    width: 1200px;
    height: 1200px;
    overflow: hidden;
    background: var(--backdrop);
  }
  .canvas {
    position: relative;
    width: 1200px;
    height: 1200px;
    display: flex;
    align-items: center;
    justify-content: center;
  }
  .business-card {
    position: relative;
    width: 1000px;
    height: 646px;
    overflow: hidden;
    background: var(--card-white);
    font-family: "Source Sans 3", "Myriad Pro", sans-serif;
  }
  .sky-backdrop {
    position: absolute;
    inset: 0;
    background:
      radial-gradient(ellipse 55% 30% at 40% 55%, rgba(255,255,255,1) 0%, rgba(255,255,255,0) 100%),
      radial-gradient(ellipse 60% 45% at 100% 100%, var(--sunset-rose) 0%, rgba(233,165,150,0) 100%),
      radial-gradient(ellipse 30% 10% at 85% 8%, rgba(236,226,232,0.7) 0%, rgba(236,226,232,0) 100%),
      linear-gradient(180deg, #ffffff 0%, #ffffff 45%, #fffaf0 62%, var(--blush) 78%, var(--sunset-gold) 90%, #f7c19a 100%);
  }
  .brand {
    position: absolute;
    left: 0;
    right: 0;
    top: 258px;
    display: flex;
    align-items: center;
    justify-content: center;
    gap: 22px;
  }
  .brand-dot {
    width: 46px;
    height: 46px;
    border-radius: 50%;
    background: var(--peach);
  }
  .brand-name {
    font-size: 60px;
    font-weight: 400;
    line-height: 1;
    letter-spacing: 1px;
    color: var(--peach);
  }
  .credentials {
    position: absolute;
    left: 0;
    right: 0;
    top: 512px;
    text-align: center;
    color: var(--text-grey);
    font-size: 22px;
    line-height: 30px;
  }
</style>
</head>
<body>
  <main class="canvas">
    <section class="business-card">
      <div class="sky-backdrop" role="img" aria-label="Céu suave ao pôr do sol em tons de branco, pêssego e rosa"></div>
      <div class="brand">
        <span class="brand-dot"></span>
        <span class="brand-name">Luciana de Macedo</span>
      </div>
      <div class="credentials">
        <p class="specialty">Cirurgiã Plástica - Estética e Reconstrutiva</p>
        <p class="registration">CRM 47.38195- 2 RQE 5716</p>
      </div>
    </section>
  </main>
</body>
</html>
```